KerrLow Farm

Need a nice simple clean double sided business card that has our logo and info on:
Kerr Low Farm
Martin & Felicity Kerr Low
kerrlowfarm@mailbarn.example
Martin: 1-780-555-0148
Felicity: 1-780-555-0193
Instagram @ kerrlow_farm

Contact Information for Business Card

Martin & Felicity Kerr Low kerrlowfarm@mailbarn.example Martin: 1-780-555-0148 Felicity: 1-780-555-0193

```html
<!DOCTYPE html>
<html lang="en">
<head>
<meta charset="utf-8">
<title>Kerr Low Farm – Business Card</title>
<link href="https://fonts.googleapis.com/css2?family=Montserrat:wght@400;500;800&display=swap" rel="stylesheet">
<style>
  :root {
    --backdrop: #bcc6c3;
    --paper: #fafaf9;
    --ink-dark: #3a3b3c;
    --ink-soft: #4a4b4c;
    --farm-green: #5d9a1e;
    --edge-green: #3f7a12;
  }
  * { margin: 0; padding: 0; box-sizing: border-box; }
  html, body {
    width: 1200px;
    height: 1080px;
    overflow: hidden;
    background: var(--backdrop);
    font-family: "Montserrat", sans-serif;
  }
  .sheet {
    width: 1200px;
    height: 1080px;
    display: flex;
    flex-direction: column;
    align-items: center;
    justify-content: center;
    gap: 40px;
  }
  .card {
    position: relative;
    width: 820px;
    height: 469px;
    background: var(--paper);
    border-bottom: 5px solid var(--edge-green);
    box-shadow: 0 14px 30px rgba(60, 70, 68, 0.25);
  }
  .owners {
    position: absolute;
    top: 62px;
    font-weight: 800;
    font-size: 34px;
    line-height: 1.32;
    letter-spacing: 0.22em;
    text-transform: uppercase;
    color: var(--ink-dark);
  }
  .contacts {
    position: absolute;
    bottom: 58px;
    list-style: none;
    font-size: 17px;
    font-weight: 400;
    letter-spacing: 0.14em;
    line-height: 1.75;
    color: var(--ink-soft);
  }
  .contacts li { display: flex; align-items: center; gap: 10px; }
  .icon { width: 13px; height: 13px; flex: none; fill: var(--ink-soft); }
  .icon-at { font-size: 13px; width: 13px; text-align: center; letter-spacing: 0; }
  .farm-name {
    position: absolute;
    font-size: 36px;
    font-weight: 500;
    letter-spacing: 0.02em;
    color: var(--farm-green);
    white-space: nowrap;
  }

  /* front: names left, farm name right */
  .card-front .owners { left: 60px; }
  .card-front .contacts { left: 60px; }
  .card-front .farm-name { right: 58px; top: 232px; }

  /* back: farm name left, names and contacts right-aligned */
  .card-back .owners { right: 60px; top: 96px; text-align: right; }
  .card-back .contacts { right: 60px; text-align: right; }
  .card-back .contacts li { justify-content: flex-end; }
  .card-back .farm-name { left: 60px; top: 78px; }
</style>
</head>
<body>
<main class="sheet">

  <section class="card card-front" aria-label="Business card front">
    <h1 class="owners">Martin &amp;<br>Felicity<br>Kerr Low</h1>
    <ul class="contacts">
      <li><svg class="icon" viewBox="0 0 16 16"><path d="M3.5 1 6 3.5 4.6 5.6c.9 2.2 3.6 4.9 5.8 5.8L12.5 10 15 12.5l-2 2.4C7.5 14.5 1.5 8.5 1.1 3z"/></svg>Martin: 1-780-555-0148</li>
      <li><svg class="icon" viewBox="0 0 16 16"><path d="M3.5 1 6 3.5 4.6 5.6c.9 2.2 3.6 4.9 5.8 5.8L12.5 10 15 12.5l-2 2.4C7.5 14.5 1.5 8.5 1.1 3z"/></svg>Felicity: 1-780-555-0193</li>
      <li><span class="icon-at">@</span>kerrlowfarm@mailbarn.example</li>
      <li><svg class="icon" viewBox="0 0 16 16"><rect x="1" y="1" width="14" height="14" rx="3"/></svg>www.photogram.example/kerrlow_farm</li>
    </ul>
    <p class="farm-name">Kerr Low Farm</p>
  </section>

  <section class="card card-back" aria-label="Business card back">
    <p class="farm-name">Kerr Low Farm</p>
    <h2 class="owners">Martin &amp;<br>Felicity<br>Kerr Low</h2>
    <ul class="contacts">
      <li>Martin: 1-780-555-0148<svg class="icon" viewBox="0 0 16 16"><path d="M3.5 1 6 3.5 4.6 5.6c.9 2.2 3.6 4.9 5.8 5.8L12.5 10 15 12.5l-2 2.4C7.5 14.5 1.5 8.5 1.1 3z"/></svg></li>
      <li>Felicity: 1-780-555-0193<svg class="icon" viewBox="0 0 16 16"><path d="M3.5 1 6 3.5 4.6 5.6c.9 2.2 3.6 4.9 5.8 5.8L12.5 10 15 12.5l-2 2.4C7.5 14.5 1.5 8.5 1.1 3z"/></svg></li>
      <li>kerrlowfarm@mailbarn.example<span class="icon-at">@</span></li>
      <li>www.photogram.example/kerrlow_farm<svg class="icon" viewBox="0 0 16 16"><rect x="1" y="1" width="14" height="14" rx="3"/></svg></li>
    </ul>
  </section>

</main>
</body>
</html>
```